Label design: Thinking outside the bottle

Vellow, a new Sydney-based natural mineral water company, is in need of a dynamic label for its range of still and lightly sparkling bottled mineral water.
Background:Vellow aims to become a leading supplier of premium mineral water in Australia and overseas, known for its purity, freshness, balanced mineral quality and, importantly, our environmental sustainability with a view to becoming carbon neutral at the earliest.
Design brief:We are looking for innovative and creative designs that will distinguish Vellow water as an up-market, high-quality bottled mineral water product. We seek to build a brand that is crisp, clean, and aesthetically interesting. We are open to designs that are experimental with shape, size, texture or transparency. The label will need to include at a minimum:
1) Vellow name and logo (see company logo attached)
2) The product name (Natural Australian spring mineral water) – with two versions for still and “lightly sparkling”.
3) A white rectangular square for the barcode located in the bottom left-hand corner.
Not essential, but we are interested in different versions that may include space for a short blurb/story of the product or a minimalist approach with no text aside from the product name and brand.
The label is for a premium product in the market. The bottle will be glass only and should avoid the impression of a large scale, mass-produced plastic bottled water. The two label attachments are a guide only as we would welcome your views and suggestions.
Target Market(s)
Premium, up-scale markets in the Middle East and Asia
Industry/Entity Type
Glass Bottle
Colors
Designer to choose colors to be used in the design.
Look and feel

```html
<!DOCTYPE html>
<html lang="en">
<head>
<meta charset="utf-8">
<title>Vellow – Lightly Sparkling Label</title>
<link href="https://fonts.googleapis.com/css2?family=Cinzel:wght@400&family=Roboto+Condensed:wght@300;400;700&display=swap" rel="stylesheet">
<style>
  :root {
    --backdrop: #f1f1f1;
    --label-black: #0e0e0e;
    --label-sheen: #3a3a3a;
    --ink-white: #ffffff;
    --ink-soft: #d6d6d6;
  }
  html, body {
    margin: 0;
    padding: 0;
    width: 900px;
    height: 1200px;
    overflow: hidden;
    background: var(--backdrop);
  }
  .canvas {
    position: relative;
    width: 900px;
    height: 1200px;
    background: var(--backdrop);
  }
  .label {
    position: absolute;
    left: 60px;
    top: 448px;
    width: 780px;
    height: 303px;
    background: var(--label-black);
    overflow: hidden;
  }
  .label__texture {
    position: absolute;
    inset: 0;
    width: 100%;
    height: 100%;
  }
  .label__content {
    position: absolute;
    inset: 0;
    text-align: center;
    color: var(--ink-white);
  }
  .brand-name {
    position: absolute;
    left: 0;
    right: 0;
    top: 58px;
    margin: 0;
    font-family: "Cinzel", serif;
    font-weight: 400;
    font-size: 84px;
    line-height: 1;
    letter-spacing: 2px;
    color: var(--ink-white);
  }
  .brand-tagline {
    position: absolute;
    left: 0;
    right: 0;
    top: 150px;
    margin: 0;
    font-family: "Roboto Condensed", sans-serif;
    font-weight: 400;
    font-size: 17px;
    letter-spacing: 0.3px;
    color: var(--ink-soft);
  }
  .product-variant {
    position: absolute;
    left: 0;
    right: 0;
    top: 222px;
    margin: 0;
    font-family: "Roboto Condensed", sans-serif;
    font-weight: 700;
    font-size: 16px;
    letter-spacing: 0.4px;
    color: var(--ink-white);
  }
  .product-volume {
    position: absolute;
    left: 0;
    right: 0;
    top: 243px;
    margin: 0;
    font-family: "Roboto Condensed", sans-serif;
    font-weight: 300;
    font-size: 15px;
    color: var(--ink-soft);
  }
</style>
</head>
<body>
  <main class="canvas">
    <section class="label">
      <svg class="label__texture" viewBox="0 0 780 303" preserveAspectRatio="none" role="img" aria-label="Fine flowing silver wave-line texture across a black band">
        <defs>
          <radialGradient id="sheen" cx="0.5" cy="0.45" r="0.7">
            <stop offset="0" stop-color="var(--label-sheen)" stop-opacity="0.9"/>
            <stop offset="0.6" stop-color="#1c1c1c"/>
            <stop offset="1" stop-color="var(--label-black)"/>
          </radialGradient>
        </defs>
        <rect width="780" height="303" fill="url(#sheen)"/>
      </svg>
      <div class="label__content">
        <h1 class="brand-name">VELLOW</h1>
        <p class="brand-tagline">PREMIUM AUSTRALIAN WATER</p>
        <p class="product-variant">LIGHTLY SPARKLING</p>
        <p class="product-volume">750ML</p>
      </div>
    </section>
  </main>
</body>
</html>
```